Custom unique Stationary design for Logistics company

We need a custom, unique , elegant and luxurious full stationary design using our new logo, following these guidelines:
1- Business card: double sided, both sides uses the navy blue as the background main color (same as the code of the navy blue used in our logo).
2- envelope and folder: also use the same navy blue as the main background color.
3- book cover( notepad cover) : same thing with the navy blue
4- letterhead: feel free to use the combination of the colors in our logo.
5- rest of the items are up to your creativity

Target Market(s)

corporates and other businesses

Industry/Entity Type

Logistics and heavy machines contractors

Requirements
Must have
• Letterhead, business card, envelope, notepad cover, paper, file
Nice to have
• navy blue to be main background color for business card, envelope, notepad cover

```html
<!DOCTYPE html>
<html lang="en">
<head>
<meta charset="UTF-8">
<title>Harbourline Freight – Business Card</title>
<link rel="stylesheet" href="https://fonts.googleapis.com/css2?family=Arimo:wght@400;700&display=swap">
<style>
  :root {
    --navy: #004c73;
    --orange: #f06033;
    --white: #ffffff;
    --stage: #b8b8b8;
    --shadow: rgba(0, 0, 0, 0.85);
  }
  * { margin: 0; padding: 0; box-sizing: border-box; }
  html, body {
    width: 1075px;
    height: 1200px;
    overflow: hidden;
    background: var(--stage);
    font-family: "Arimo", Arial, sans-serif;
  }
  .card {
    position: absolute;
    left: 206px;
    width: 663px;
    height: 396px;
    background: var(--navy);
    box-shadow: 3px 3px 0 var(--shadow);
    overflow: hidden;
  }
  .card--front { top: 187px; }
  .card--back { top: 637px; }

  .card__backdrop { position: absolute; inset: 0; width: 100%; height: 100%; }

  .holder {
    position: absolute;
    top: 228px;
    left: 0;
    width: 100%;
    text-align: center;
  }
  .holder__name {
    color: var(--orange);
    font-size: 23px;
    font-weight: 400;
    letter-spacing: 0.2px;
  }
  .holder__role {
    color: var(--white);
    font-size: 18px;
    margin-top: 2px;
  }

  .contacts {
    position: absolute;
    left: 36px;
    top: 292px;
    list-style: none;
    color: var(--white);
    font-size: 18px;
    line-height: 24px;
  }
  .contacts li { display: flex; align-items: center; gap: 6px; }
  .contacts svg { width: 17px; height: 17px; flex: none; }

  .address {
    position: absolute;
    right: 40px;
    top: 318px;
    color: var(--white);
    font-size: 18px;
    line-height: 24px;
    text-align: right;
    font-style: normal;
  }

  .brand {
    position: absolute;
    top: 0; left: 0;
    width: 100%; height: 100%;
    display: flex;
    align-items: center;
    justify-content: center;
    color: var(--white);
    font-size: 44px;
    font-weight: 700;
    letter-spacing: 1px;
  }
</style>
</head>
<body>
  <section class="card card--front">
    <svg class="card__backdrop" viewBox="0 0 663 396" aria-hidden="true">
      <rect width="663" height="396" fill="var(--orange)"/>
      <path d="M0 225 Q330 -60 663 234 L663 396 L0 396 Z" fill="var(--navy)"/>
    </svg>

    <div class="holder">
      <h1 class="holder__name">MARCUS HALE</h1>
      <p class="holder__role">Managing Director</p>
    </div>

    <ul class="contacts">
      <li>
        <svg viewBox="0 0 24 24" aria-hidden="true"><path fill="var(--orange)" d="M6.6 10.8a15 15 0 0 0 6.6 6.6l2.2-2.2a1 1 0 0 1 1-.25 11.4 11.4 0 0 0 3.6.57 1 1 0 0 1 1 1V20a1 1 0 0 1-1 1A17 17 0 0 1 3 4a1 1 0 0 1 1-1h3.5a1 1 0 0 1 1 1c0 1.25.2 2.45.57 3.57a1 1 0 0 1-.25 1z"/></svg>
        044-987 654 321
      </li>
      <li>
        <svg viewBox="0 0 24 24" aria-hidden="true"><rect x="2" y="5" width="20" height="14" fill="var(--orange)"/><path d="M2 5l10 8 10-8" fill="none" stroke="var(--navy)" stroke-width="1.8"/></svg>
        info@harbourline.com
      </li>
      <li>
        <svg viewBox="0 0 24 24" aria-hidden="true"><g fill="none" stroke="var(--orange)" stroke-width="2"><circle cx="12" cy="12" r="9"/><ellipse cx="12" cy="12" rx="4" ry="9"/><path d="M3 12h18M5 7h14M5 17h14"/></g></svg>
        www.harbourline.com
      </li>
    </ul>

    <address class="address">
      17, Harbour Road, Dock Quarter<br>
      30218, Country Name
    </address>
  </section>

  <section class="card card--back">
    <p class="brand">Harbourline Freight</p>
  </section>
</body>
</html>
```